World Class Presentation folder for a National Designer of innovative building products

We are a National Designer, Manufacturer, and distributor of aluminum and stainless Balconies, Railings, Sunshades, and Patio Covers. We sell our products and services to the very best commercial condo and residential builders in the country. This Brochure folder will be the first piece of literature that we give to our customers, and want to WOW them at first glance with a world-class design and look.

We already have a logo and website but would like you to visit https://velmorafabworks.example and view the projects and product information to help inspire you to create an award-winning piece of literature for us.

Besides putting literature in it, the folder must have a place to hold a business card.

Thank you in advance for your great designs, and I look forward to working with you.
Dolan Fratheringe
President | Pacific, WA
418.627.5190 ext 305

```html
<!DOCTYPE html>
<html lang="en">
<head>
<meta charset="utf-8">
<title>Velmora Fabworks – Presentation Folder</title>
<link href="https://fonts.googleapis.com/css2?family=Montserrat:wght@600;800&family=Oswald:wght@500;600&family=Source+Sans+3:wght@400&display=swap" rel="stylesheet">
<style>
  :root{
    --ink:#2d2d2e;
    --ink-deep:#232324;
    --crimson:#c8184a;
    --crimson-dark:#a3123b;
    --paper:#ffffff;
    --mist:#e6e6e6;
    --stage:#d8d8d8;
    --text-light:#f1f1f1;
  }
  html,body{margin:0;padding:0;width:1200px;height:1032px;overflow:hidden;background:var(--stage);}
  .folder{position:absolute;left:168px;top:73px;width:864px;height:886px;}
  .folder-art{position:absolute;inset:0;width:864px;height:886px;}
  .band-title{position:absolute;top:136px;height:32px;line-height:32px;margin:0;font:600 14.5px/32px "Montserrat",sans-serif;color:var(--paper);letter-spacing:-0.3px;white-space:nowrap;}
  .band-title--left{left:30px;}
  .band-title--right{left:461px;}
  .brand{position:absolute;display:flex;align-items:center;gap:8px;margin:0;font-family:"Montserrat",sans-serif;font-weight:800;line-height:1;}
  .brand-mark{border-radius:50%;background:var(--crimson);flex:none;}
  .brand--cover{left:590px;top:38px;font-size:29px;color:var(--ink);}
  .brand--cover .brand-mark{width:22px;height:22px;}
  .brand--inside{left:168px;top:55px;font-size:15px;color:var(--crimson);}
  .brand--inside .brand-mark{width:10px;height:10px;}
  .products{position:absolute;left:37px;top:184px;}
  .products-title{margin:0 0 8px;font:600 25px/32px "Oswald",sans-serif;color:var(--crimson);letter-spacing:-0.2px;}
  .product-list{list-style:none;margin:0;padding:0;}
  .product-list li{position:relative;padding-left:17px;font:400 13px/22.6px "Source Sans 3",sans-serif;color:var(--text-light);}
  .product-list li svg{position:absolute;left:0;top:6px;}
  .contact{position:absolute;left:18px;top:593px;list-style:none;margin:0;padding:0;}
  .contact li{display:flex;align-items:center;gap:7px;height:23px;font:400 12.5px/1 "Source Sans 3",sans-serif;color:var(--text-light);}
  .contact-icon{width:16px;height:16px;border-radius:3px;background:var(--crimson);display:flex;align-items:center;justify-content:center;}
  .cover-headline{position:absolute;left:449px;top:562px;margin:0;font:500 16.5px/25px "Oswald",sans-serif;color:var(--ink);letter-spacing:-0.3px;text-transform:uppercase;}
  .cover-url{position:absolute;left:466px;top:650px;font:400 12px/16px "Source Sans 3",sans-serif;color:var(--paper);}
</style>
</head>
<body>
<div class="folder">
  <svg class="folder-art" viewBox="0 0 864 886" xmlns="http://www.w3.org/2000/svg">
    <!-- top panel base -->
    <rect x="0" y="0" width="864" height="683" fill="var(--paper)"/>
    <polygon points="114,0 559,0 485,136 0,136" fill="var(--ink)"/>
    <rect x="0" y="168" width="432" height="515" fill="var(--ink)"/>
    <!-- cover photo -->
    <polygon role="img" aria-label="Rooftop terrace with wicker lounge chairs, planters and aluminium railing below city towers"
      points="467,168 864,168 864,530 440,530 330,445" fill="url(#terrace)"/>
    <!-- white lower cover area -->
    <rect x="432" y="530" width="432" height="153" fill="var(--paper)"/>
    <polygon points="864,352 662,683 690,683 864,392" fill="var(--mist)"/>
    <polygon points="864,375 682,683 864,683" fill="var(--crimson)"/>
    <!-- inside white corner -->
    <polygon points="280,551 432,551 432,683 183,683" fill="var(--paper)"/>
    <!-- project tiles -->
    <polygon role="img" aria-label="Glass and aluminium railing along a city plaza" points="67,445 243,445 188,551 10,551" fill="url(#tileA)"/>
    <polygon role="img" aria-label="Apartment building with balconies over a green lawn" points="251,445 433,445 378,551 196,551" fill="url(#tileB)"/>
    <polygon role="img" aria-label="White patio cover over a backyard deck" points="441,445 607,445 557,551 386,551" fill="url(#tileC)"/>
    <!-- red band -->
    <rect x="0" y="136" width="864" height="32" fill="var(--crimson)"/>
    <line x1="432" y1="136" x2="432" y2="168" stroke="var(--crimson-dark)" stroke-width="1"/>
    <!-- faint badges -->
    <circle cx="290" cy="298" r="44" fill="none" stroke="#6b6b6b" stroke-width="4" opacity="0.6"/>
    <circle cx="290" cy="298" r="33" fill="#555" opacity="0.45"/>
    <circle cx="800" cy="616" r="37" fill="none" stroke="#e06487" stroke-width="4" opacity="0.7"/>
    <circle cx="800" cy="616" r="27" fill="#d83a66" opacity="0.6"/>
    <!-- value icons -->
    <g fill="none" stroke="var(--crimson)" stroke-width="3">
      <circle cx="56" cy="402" r="16"/><circle cx="111" cy="402" r="16"/><circle cx="171" cy="402" r="16"/>
    </g>
    <!-- spec listing badge -->
    <rect x="261" y="608" width="141" height="45" rx="3" fill="var(--crimson)"/>
    <!-- url pill -->
    <polygon points="434,647 640,647 648,668 434,668" fill="var(--crimson)"/>
    <circle cx="455" cy="657.5" r="5" fill="none" stroke="var(--paper)" stroke-width="1.2"/>
    <line x1="450" y1="657.5" x2="460" y2="657.5" stroke="var(--paper)" stroke-width="1"/>
    <ellipse cx="455" cy="657.5" rx="2.2" ry="5" fill="none" stroke="var(--paper)" stroke-width="1"/>
    <!-- pockets -->
    <polygon points="0,683 432,683 410,886 0,886" fill="var(--ink)"/>
    <polygon points="432,683 864,683 864,886 455,886" fill="var(--ink)"/>
    <line x1="112" y1="750" x2="140" y2="725" stroke="#3c3c3d" stroke-width="1"/>
    <line x1="285" y1="843" x2="313" y2="818" stroke="#3c3c3d" stroke-width="1"/>
    <defs>
      <linearGradient id="terrace" x1="0" y1="0" x2="0" y2="1">
        <stop offset="0" stop-color="#8fb3d6"/><stop offset="0.35" stop-color="#a8a08a"/>
        <stop offset="0.6" stop-color="#5f6b3a"/><stop offset="1" stop-color="#4a4542"/>
      </linearGradient>
      <linearGradient id="tileA" x1="0" y1="0" x2="0" y2="1">
        <stop offset="0" stop-color="#7a8a9a"/><stop offset="1" stop-color="#3b3d3c"/>
      </linearGradient>
      <linearGradient id="tileB" x1="0" y1="0" x2="0" y2="1">
        <stop offset="0" stop-color="#b2c2d2"/><stop offset="0.55" stop-color="#8a6a5a"/><stop offset="1" stop-color="#5f8f3a"/>
      </linearGradient>
      <linearGradient id="tileC" x1="0" y1="0" x2="0" y2="1">
        <stop offset="0" stop-color="#c9d3dc"/><stop offset="0.5" stop-color="#e8e6e0"/><stop offset="1" stop-color="#6f8f4a"/>
      </linearGradient>
    </defs>
  </svg>

  <p class="brand brand--inside"><span class="brand-mark"></span>VELMORA FABWORKS</p>
  <p class="brand brand--cover"><span class="brand-mark"></span>VELMORA<br>FABWORKS</p>

  <h2 class="band-title band-title--left">MAINTENANCE FREE FACTORY UNIFORM ASSEMBLY</h2>
  <h2 class="band-title band-title--right">STUNNING RESULTS APPLICATIONS TO INSPIRE</h2>

  <section class="products">
    <h3 class="products-title">OUR PRODUCTS</h3>
    <ul class="product-list">
      <li><svg width="11" height="11" viewBox="0 0 11 11"><circle cx="5.5" cy="5.5" r="4.8" fill="none" stroke="#c8184a" stroke-width="1.2"/><path d="M3.2 5.6l1.6 1.6 3-3" fill="none" stroke="#c8184a" stroke-width="1.2"/></svg>Railling System</li>
      <li><svg width="11" height="11" viewBox="0 0 11 11"><circle cx="5.5" cy="5.5" r="4.8" fill="none" stroke="#c8184a" stroke-width="1.2"/><path d="M3.2 5.6l1.6 1.6 3-3" fill="none" stroke="#c8184a" stroke-width="1.2"/></svg>Stainless Steel Cable</li>
      <li><svg width="11" height="11" viewBox="0 0 11 11"><circle cx="5.5" cy="5.5" r="4.8" fill="none" stroke="#c8184a" stroke-width="1.2"/><path d="M3.2 5.6l1.6 1.6 3-3" fill="none" stroke="#c8184a" stroke-width="1.2"/></svg>Balcony Systems</li>
      <li><svg width="11" height="11" viewBox="0 0 11 11"><circle cx="5.5" cy="5.5" r="4.8" fill="none" stroke="#c8184a" stroke-width="1.2"/><path d="M3.2 5.6l1.6 1.6 3-3" fill="none" stroke="#c8184a" stroke-width="1.2"/></svg>Sunshade Systems</li>
      <li><svg width="11" height="11" viewBox="0 0 11 11"><circle cx="5.5" cy="5.5" r="4.8" fill="none" stroke="#c8184a" stroke-width="1.2"/><path d="M3.2 5.6l1.6 1.6 3-3" fill="none" stroke="#c8184a" stroke-width="1.2"/></svg>Canopy Systems</li>
      <li><svg width="11" height="11" viewBox="0 0 11 11"><circle cx="5.5" cy="5.5" r="4.8" fill="none" stroke="#c8184a" stroke-width="1.2"/><path d="M3.2 5.6l1.6 1.6 3-3" fill="none" stroke="#c8184a" stroke-width="1.2"/></svg>Pation Cover Systems</li>
    </ul>
  </section>

  <ul class="contact">
    <li><span class="contact-icon"><svg width="10" height="10" viewBox="0 0 10 10"><path d="M2 1l2 2-1 1.2c.6 1.2 1.6 2.2 2.8 2.8L7 6l2 2-1.3 1.3C4.6 9 1 5.4.7 2.3z" fill="#fff"/></svg></span>866-410-2275</li>
    <li><span class="contact-icon"><svg width="10" height="8" viewBox="0 0 10 8"><rect x="0.5" y="0.5" width="9" height="7" fill="none" stroke="#fff"/><path d="M0.5 0.5l4.5 4 4.5-4" fill="none" stroke="#fff"/></svg></span>dolan@velmorafabworks.example</li>
    <li><span class="contact-icon"><svg width="10" height="10" viewBox="0 0 10 10"><circle cx="5" cy="5" r="4" fill="none" stroke="#fff"/><line x1="1" y1="5" x2="9" y2="5" stroke="#fff" stroke-width="0.8"/></svg></span>velmorafabworks.example</li>
  </ul>

  <h1 class="cover-headline">Premier manufacturer &amp; distributer<br>of aluminum railing, balcony, and<br>sunshade systems</h1>
  <span class="cover-url">velmorafabworks.example</span>
</div>
</body>
</html>
```